Brell Harbor Company Business Cards

Front and Back Business Card - logo and text setup - cool design. I need workable photoshop or illustrator files so I can setup each employee card with design that is created
Updates

Hi everyone, thank you for the great entries. Please no more white and blue cards - there are so many already - black and silver only now please. thanks!

Target Market(s)

Construction Industry - Facility Managers

Industry/Entity Type

Construction

Contact Information for Business Card

I really like contemporary simplistic looks - clean neat....not opposed to seeing some black backrounds

Requirements
Must have
• Logo/website address with design on front only - www.brellharbor-example.com (logo attached)
• Back:
• Name/Title/Company Address/Phone/email address
Nice to have
• Cool design
Should not have
• Nothing gimmicky like Fire or Water - since we are a Fire Protection company - it has all been done

```html
<!DOCTYPE html>
<html lang="en">
<head>
<meta charset="utf-8">
<title>Brell Harbor Company – Business Card</title>
<link rel="stylesheet" href="https://fonts.googleapis.com/css2?family=Arimo:ital,wght@0,400;0,700;1,400&display=swap">
<style>
  :root {
    --paper: #ffffff;
    --black: #141414;
    --charcoal: #2b2b2b;
    --silver-light: #e4e4e4;
    --silver: #b9b9b9;
    --silver-dark: #8c8c8c;
    --ink: #111111;
    --photo-light: #cfcfcf;
    --photo-dark: #2a2a2a;
  }
  html, body {
    margin: 0;
    padding: 0;
    width: 1200px;
    height: 686px;
    overflow: hidden;
    background: var(--paper);
  }
  .card {
    position: relative;
    width: 1200px;
    height: 686px;
    background: var(--paper);
    font-family: "Arimo", Arial, sans-serif;
    color: var(--ink);
    overflow: hidden;
  }
  .brand {
    position: absolute;
    left: 140px;
    top: 50px;
    display: flex;
    align-items: center;
    gap: 12px;
    font-weight: 700;
    font-size: 46px;
    line-height: 1;
    letter-spacing: -0.5px;
    color: var(--black);
  }
  .brand-mark {
    width: 16px;
    height: 16px;
    background: var(--silver-dark);
  }
  .website {
    position: absolute;
    left: 168px;
    top: 106px;
    font-size: 20px;
    line-height: 1;
    color: var(--silver-dark);
    letter-spacing: 0.3px;
  }
  .portrait-frame {
    position: absolute;
    left: 122px;
    top: 218px;
    width: 272px;
    height: 339px;
    background: var(--black);
  }
  .nameplate {
    position: absolute;
    left: 388px;
    top: 276px;
    width: 637px;
    height: 162px;
    box-sizing: border-box;
    background: linear-gradient(180deg, var(--silver-light) 0%, var(--silver) 100%);
    border: 4px solid var(--charcoal);
    border-radius: 3px;
  }
  .portrait {
    position: absolute;
    left: 117px;
    top: 183px;
    width: 310px;
    height: 374px;
    background: linear-gradient(180deg, var(--photo-light) 0%, #9a9a9a 28%, var(--photo-dark) 52%, var(--photo-dark) 100%);
    clip-path: polygon(35% 0, 65% 0, 72% 18%, 70% 30%, 95% 40%, 100% 100%, 0 100%, 3% 42%, 30% 30%, 28% 18%);
  }
  .person-name {
    position: absolute;
    left: 600px;
    top: 300px;
    width: 420px;
    text-align: center;
    font-size: 50px;
    line-height: 1;
    color: var(--ink);
  }
  .person-name strong { font-weight: 700; }
  .person-title {
    position: absolute;
    left: 600px;
    top: 382px;
    width: 420px;
    text-align: center;
    font-style: italic;
    font-size: 37px;
    line-height: 1;
    color: var(--ink);
  }
  .contact {
    position: absolute;
    left: 0;
    top: 622px;
    width: 1200px;
    text-align: center;
    font-size: 30px;
    line-height: 1;
    color: var(--ink);
    white-space: nowrap;
  }
  .contact .sep { color: var(--silver-dark); padding: 0 6px; }
</style>
</head>
<body>
  <div class="card">
    <div class="brand"><span class="brand-mark"></span>Brell Harbor</div>
    <div class="website">www.brellharbor-example.com</div>

    <div class="portrait-frame"></div>
    <div class="nameplate"></div>
    <div class="portrait" role="img" aria-label="Portrait photo of the employee in a dark suit"></div>

    <div class="person-name">Mara <strong>Lintel</strong></div>
    <div class="person-title">Marketing director</div>

    <div class="contact">4580, Corvane st. , Westmere, Canada<span class="sep">|</span>+1555014382<span class="sep">|</span>maralintel@example.com</div>
  </div>
</body>
</html>
```